business card design for a small scale specialty cut flower farm

We need a business card design for Hollowmere Bloom Farm based in Langley, BC, Canada. We produce specialty, high-end cut flowers and sell locally to florists, local shops and markets and the end user through bouquet subscriptions. The final business card design should be memorable and have a timeless or vintage feel. We would prefer a square shape.
Updates

Target Market(s)

florists, shops and seasonal markets, local flower lovers

Industry/Entity Type

Floral

Contact Information for Business Card

Tamsin Ellery Voss, Grower
Langley, BC, Canada
website: hollowmerebloomfarm.example
instagram: @hollowmerebloomfarm
Tel: 555.317.4290
facebook: www.facebook.example/hollowmereblooms/

Font styles to use
Serif
Decorative
Script

Requirements
Must have
• soft black background colour on front side, the included logo and catch phrase: Fresh Local Seasonal
Nice to have
• phone number and website address on front of card, included photo 6539 incorporated onto the back, possibly photo 6609 as well.

```html
<!DOCTYPE html>
<html lang="en">
<head>
<meta charset="utf-8">
<title>Hollowmere Bloom Farm – Business Card</title>
<link rel="stylesheet" href="https://fonts.googleapis.com/css2?family=Roboto+Condensed:wght@300;400&family=Lato:ital,wght@0,300;0,400;1,300&display=swap">
<style>
  :root {
    --page: #f3f2ef;
    --card: #31250f;
    --rule: #ece9e4;
    --ink: #ffffff;
    --accent: #e2a8cf;
    --bloom: #eab8d6;
  }
  * { margin: 0; padding: 0; box-sizing: border-box; }
  html, body { width: 1200px; height: 1200px; overflow: hidden; background: var(--page); }
  .canvas { position: relative; width: 1200px; height: 1200px; }

  .card {
    position: absolute; top: 330px; width: 540px; height: 540px;
    background: var(--card); color: var(--ink);
    font-family: "Roboto Condensed", Arial, sans-serif;
  }
  .card--front { left: 40px; }
  .card--back { left: 620px; }

  /* rules with dot ends */
  .rule { position: absolute; background: var(--rule); }
  .rule::before, .rule::after {
    content: ""; position: absolute; width: 6px; height: 6px;
    border-radius: 50%; background: var(--rule);
  }
  .rule--v { width: 1px; }
  .rule--v::before { top: -3px; left: -2.5px; }
  .rule--v::after { bottom: -3px; left: -2.5px; }
  .rule--h { height: 1px; }
  .rule--h::before { left: -3px; top: -2.5px; }
  .rule--h::after { right: -3px; top: -2.5px; }

  /* logo lockup */
  .logo { position: absolute; text-align: center; transform: translateX(-50%); }
  .logo__bloom { display: block; margin: 0 auto; border-radius: 50%; background: var(--bloom); }
  .logo__name {
    font-family: "Roboto Condensed", Arial, sans-serif; font-weight: 300;
    color: var(--ink); letter-spacing: 0.14em; text-transform: uppercase;
    line-height: 1.2; white-space: nowrap;
  }
  .logo__tagline {
    font-family: "Lato", Arial, sans-serif; font-style: italic; font-weight: 300;
    color: var(--ink); white-space: nowrap;
  }
  .logo__est {
    font-family: "Lato", Arial, sans-serif; font-weight: 400;
    letter-spacing: 0.45em; color: var(--ink); white-space: nowrap;
  }

  .card--front .logo { left: 122px; top: 168px; }
  .card--front .logo__bloom { width: 70px; height: 70px; }
  .card--front .logo__name { font-size: 19px; margin-top: 22px; }
  .card--front .logo__tagline { font-size: 12px; margin-top: 10px; }
  .card--front .logo__est { font-size: 8px; margin-top: 10px; }

  .card--back .logo { left: 270px; top: 112px; }
  .card--back .logo__bloom { width: 112px; height: 112px; }
  .card--back .logo__name { font-size: 28px; margin-top: 38px; }
  .card--back .logo__tagline { font-size: 18px; margin-top: 16px; }
  .card--back .logo__est { font-size: 11px; margin-top: 14px; }

  /* identity */
  .person { position: absolute; left: 266px; top: 70px; }
  .person__name { font-size: 25px; font-weight: 400; color: var(--accent); line-height: 1.1; white-space: nowrap; }
  .person__role { font-size: 19px; font-weight: 400; color: var(--ink); line-height: 1.35; }

  /* contacts */
  .contacts { position: absolute; left: 262px; top: 208px; list-style: none; }
  .contacts__item { display: flex; align-items: center; height: 40px; font-size: 18px; font-weight: 300; white-space: nowrap; }
  .contacts__icon { width: 17px; height: 17px; margin-right: 12px; color: var(--accent); flex: none; }
  .contacts__dot { width: 10px; height: 10px; border-radius: 50%; background: var(--accent); margin: 0 15px 0 4px; flex: none; }
</style>
</head>
<body>
<main class="canvas">

  <section class="card card--front" aria-label="Card front">
    <div class="logo">
      <span class="logo__bloom" role="img" aria-label="Watercolour wild rose with leaves"></span>
      <p class="logo__name">Hollowmere<br>Bloom Farm</p>
      <p class="logo__tagline">Fresh Local Seasonal</p>
      <p class="logo__est">EST.2019</p>
    </div>

    <div class="rule rule--v" style="left:243px; top:170px; height:232px;"></div>

    <div class="person">
      <p class="person__name">Tamsin Ellery Voss</p>
      <p class="person__role">Grower</p>
    </div>

    <ul class="contacts">
      <li class="contacts__item">
        <svg class="contacts__icon" viewBox="0 0 24 24" aria-hidden="true">
          <path fill="currentColor" d="M2 9c0-2 4-4 10-4s10 2 10 4v2h-5V9c-1-.6-3-1-5-1s-4 .4-5 1v2H2z"/>
          <path fill="currentColor" d="M7 11h10l3 8H4z"/>
          <circle cx="12" cy="15" r="2.2" fill="#31250f"/>
        </svg>
        (555) 317-4290
      </li>
      <li class="contacts__item"><span class="contacts__dot" aria-hidden="true"></span>hollowmereblooms</li>
      <li class="contacts__item"><span class="contacts__dot" aria-hidden="true"></span>@hollowmerebloomfarm</li>
      <li class="contacts__item">
        <svg class="contacts__icon" viewBox="0 0 24 24" aria-hidden="true" fill="none" stroke="currentColor" stroke-width="1.6">
          <circle cx="12" cy="12" r="9.5"/>
          <ellipse cx="12" cy="12" rx="4.2" ry="9.5"/>
          <path d="M2.5 12h19M4 7h16M4 17h16M12 2.5v19"/>
        </svg>
        hollowmerebloomfarm.example
      </li>
    </ul>

    <div class="rule rule--h" style="left:56px; top:470px; width:428px;"></div>
  </section>

  <section class="card card--back" aria-label="Card back">
    <div class="rule rule--v" style="left:40px; top:246px; height:96px;"></div>
    <div class="rule rule--v" style="left:499px; top:246px; height:96px;"></div>

    <div class="logo">
      <span class="logo__bloom" role="img" aria-label="Watercolour wild rose with leaves"></span>
      <p class="logo__name">Hollowmere Bloom Farm</p>
      <p class="logo__tagline">Fresh Local Seasonal</p>
      <p class="logo__est">EST.2019</p>
    </div>
  </section>

</main>
</body>
</html>
```